Hip surgeon needs a educative book cover design

I need to re-design my old book cover for its 3rd edition.
It's a small book dedicated to my patients, who underwent total hip replacement. It's meant to help people getting around the basic care after a total hip replacement surgery and getting back to their normal, active life.
The title is: "Bright mornings: a walking companion guide".
I already had a new logo, new stationery and new website design from PixelHarbor (please see the attachments).
The final design should be look alike the other fresh new designs. It must communicate health, peacefulness.
I also attached the manual as it looks today for reference.
A5 size.
Just cover and back cover.

```html
<!DOCTYPE html>
<html lang="en">
<head>
<meta charset="UTF-8">
<title>Bright Mornings – A Walking Companion Guide – Covers</title>
<link href="https://fonts.googleapis.com/css2?family=Open+Sans:wght@400;600;700&display=swap" rel="stylesheet">
<style>
  :root {
    --bg: #e9ecef;
    --blue-deep: #0b4fa0;
    --blue-main: #1666c0;
    --blue-bright: #2a8ad8;
    --blue-title: #1f6db8;
    --ink: #3a3f45;
    --white: #ffffff;
    --panel: #eef1f4;
    --panel-edge: #9aa3ad;
  }
  * { box-sizing: border-box; margin: 0; padding: 0; }
  html, body { width: 1200px; height: 800px; overflow: hidden; }
  body {
    background: var(--bg);
    font-family: "Open Sans", Arial, sans-serif;
    position: relative;
  }
  .cover {
    position: absolute;
    top: 80px;
    width: 452px;
    height: 640px;
    overflow: hidden;
    box-shadow: 0 6px 24px rgba(0,0,0,.18);
  }

  /* Blue cover */
  .cover--blue {
    left: 110px;
    background: linear-gradient(180deg, var(--blue-main) 0%, var(--blue-deep) 100%);
  }
  .cover--blue .band-light {
    position: absolute;
    left: 0; right: 0;
    top: 214px; height: 292px;
    background: linear-gradient(180deg, var(--blue-bright), #2f95de);
  }
  .cover--blue .band-line {
    position: absolute; left: 0; right: 0; height: 3px;
    background: rgba(255,255,255,.18);
  }
  .cover--blue .title-block {
    position: absolute; top: 118px; left: 0; right: 0;
    text-align: center; color: var(--white);
  }
  .cover--blue .title {
    font-size: 30px; font-weight: 600; line-height: 1.12;
  }
  .cover--blue .subtitle {
    font-size: 17px; font-weight: 400; margin-top: 4px;
  }
  .cover--blue .brand {
    position: absolute; top: 558px; left: 0; right: 0;
    display: flex; justify-content: center;
  }

  /* White cover */
  .cover--white {
    left: 638px;
    background: var(--white);
  }
  .cover--white .spine-band {
    position: absolute; top: 0; bottom: 0; left: 26px; width: 28px;
    background: var(--blue-main);
  }
  .cover--white .spine-band::after {
    content: ""; position: absolute; top: 0; bottom: 0; left: 8px; width: 12px;
    background: var(--blue-bright);
  }
  .cover--white .title-block {
    position: absolute; top: 40px; left: 74px; right: 20px;
  }
  .cover--white .title {
    color: var(--blue-title);
    font-size: 44px; font-weight: 600; line-height: 1.08;
  }
  .cover--white .subtitle {
    color: var(--ink);
    font-size: 24px; font-weight: 400; margin-top: 12px;
  }
  .cover--white .brand { margin-top: 20px; }

  .brand {
    display: flex; align-items: center; gap: 7px;
  }
  .brand-dot {
    width: 18px; height: 18px; border-radius: 50%;
    background: var(--blue-main);
  }
  .cover--blue .brand-dot { background: var(--white); }
  .brand-name {
    font-size: 11px; font-weight: 600; line-height: 1.2;
    color: var(--blue-main);
  }
  .cover--blue .brand-name { color: var(--white); }
  .brand-name span { display: block; font-weight: 600; }

  .illustration {
    position: absolute; left: 150px; top: 300px; width: 290px; height: 310px;
    background: linear-gradient(160deg, var(--panel), #dfe4e9);
    border: 1px solid var(--panel-edge);
  }
</style>
</head>
<body>

  <section class="cover cover--blue" aria-label="Back cover">
    <div class="band-light"></div>
    <div class="band-line" style="top:214px"></div>
    <div class="band-line" style="top:503px"></div>
    <div class="title-block">
      <h2 class="title">Bright Mornings</h2>
      <p class="subtitle">A Walking Companion Guide</p>
    </div>
    <div class="brand">
      <div class="brand-dot"></div>
      <p class="brand-name">Dr. Elena M. Varga<span>Cirurgia do Quadril</span></p>
    </div>
  </section>

  <section class="cover cover--white" aria-label="Front cover">
    <div class="spine-band"></div>
    <div class="title-block">
      <h1 class="title">Bright<br>Mornings</h1>
      <p class="subtitle">A Walking Companion Guide</p>
      <div class="brand">
        <div class="brand-dot"></div>
        <p class="brand-name">Dr. Elena M. Varga<span>Cirurgia do Quadril</span></p>
      </div>
    </div>
    <div class="illustration" role="img" aria-label="Sketched panels of a recovering patient walking with crutches, sitting, kneeling and climbing stairs"></div>
  </section>

</body>
</html>
```